Tellwick Asset Management - Corporate Letter Head Project

Looking for a classy design based on our current logo. Please find current logo source file in files. With our color scheme.

Target Market(s)

We're an investment firm, the letterhead needs to look professional and attractive to clients.

Industry/Entity Type

Hedgefund

Colors
0054AA
0677BA
7BADD7
CADEEF
E8F1F8

Requirements
Must have
• Our logo, address, phone number, and email

```html
<!DOCTYPE html>
<html lang="en">
<head>
<meta charset="utf-8">
<title>Tellwick Asset Management — Letterhead</title>
<link href="https://fonts.googleapis.com/css2?family=Roboto:wght@400;500;700&display=swap" rel="stylesheet">
<style>
  :root {
    --ink: #000000;
    --navy: #1b365d;
    --sky: #009bdc;
    --royal: #0a5cb0;
    --paper: #ffffff;
    --ghost: #f4f6f8;
  }
  html, body {
    margin: 0;
    padding: 0;
    overflow: hidden;
    background: var(--paper);
  }
  .letterhead {
    position: relative;
    width: 848px;
    height: 1200px;
    overflow: hidden;
    background: var(--paper);
    font-family: "Roboto", Arial, sans-serif;
  }
  .top-band {
    position: absolute;
    left: 0;
    top: 0;
    width: 848px;
    height: 26px;
    background: var(--ink);
  }
  .bottom-band {
    position: absolute;
    left: 0;
    bottom: 0;
    width: 848px;
    height: 28px;
    background: var(--ink);
  }
  .corner-accent {
    position: absolute;
    width: 190px;
    height: 110px;
    background: linear-gradient(135deg, var(--royal), var(--sky));
  }
  .corner-accent.top-left {
    left: 0;
    top: 0;
    clip-path: polygon(0 0, 100% 0, 0 100%);
  }
  .corner-accent.bottom-right {
    right: 0;
    bottom: 0;
    width: 230px;
    height: 130px;
    clip-path: polygon(100% 0, 100% 100%, 0 100%);
  }
  .brand {
    position: absolute;
    left: 88px;
    top: 78px;
    display: flex;
    align-items: center;
    gap: 14px;
  }
  .brand-mark {
    width: 62px;
    height: 62px;
    box-sizing: border-box;
    border: 1.5px solid var(--navy);
  }
  .brand-name {
    margin: 0;
    font-weight: 500;
    font-size: 27px;
    line-height: 1.05;
    color: var(--navy);
  }
  .contact {
    position: absolute;
    right: 40px;
    top: 94px;
    text-align: right;
    font-size: 13.5px;
    color: var(--ink);
  }
  .contact-line {
    display: flex;
    justify-content: flex-end;
    align-items: center;
    gap: 10px;
    height: 20px;
    margin-bottom: 6px;
  }
  .contact-line.phone { font-weight: 700; }
  .contact-icon { width: 12px; height: 14px; fill: var(--sky); }
  .header-rule {
    position: absolute;
    left: 88px;
    top: 168px;
    width: 715px;
    height: 3px;
    display: flex;
  }
  .header-rule .rule-dark { width: 291px; background: var(--navy); }
  .header-rule .rule-light { flex: 1; background: var(--sky); }
  .backdrop-square {
    position: absolute;
    left: 291px;
    top: 481px;
    width: 264px;
    height: 262px;
    background: var(--ghost);
  }
</style>
</head>
<body>
<main class="letterhead">
  <div class="top-band"></div>
  <div class="corner-accent top-left" role="img" aria-label="Angled blue corner graphic"></div>
  <div class="bottom-band"></div>
  <div class="corner-accent bottom-right" role="img" aria-label="Angled blue corner graphic"></div>

  <header>
    <div class="brand">
      <div class="brand-mark"></div>
      <p class="brand-name">Tellwick Asset<br>Management</p>
    </div>

    <div class="contact">
      <div class="contact-line address">
        <span>123, Lorem Ipsum, City State Country</span>
        <svg class="contact-icon" viewBox="0 0 12 16"><path d="M6 0C2.7 0 0 2.6 0 5.9 0 10 6 16 6 16s6-6 6-10.1C12 2.6 9.3 0 6 0zm0 8.3a2.4 2.4 0 1 1 0-4.8 2.4 2.4 0 0 1 0 4.8z"/></svg>
      </div>
      <div class="contact-line phone">
        <span>123 456 7890, 123 456 7890</span>
        <svg class="contact-icon" viewBox="0 0 16 16"><path d="M3.6 0.5l2.3 2.9c.4.5.3 1.1-.1 1.5L4.5 6c.9 2 2.6 3.7 4.6 4.7l1.2-1.3c.4-.4 1.1-.5 1.5-.1l2.9 2.2c.5.4.6 1.1.2 1.6l-1.5 1.8c-.5.6-1.3.8-2 .5C6.5 13.8 2.3 9.6.7 4.6.5 3.9.7 3.1 1.3 2.6L3 .4c.2-.2.4-.1.6.1z"/></svg>
      </div>
    </div>

    <div class="header-rule">
      <span class="rule-dark"></span>
      <span class="rule-light"></span>
    </div>
  </header>

  <div class="backdrop-square" aria-hidden="true"></div>
</main>
</body>
</html>
```